Healthy living company needs logo / business card

We are looking for a business identity for our company that operates in the Health and Wellness area.
Our audience is those open to hearing about the links between ill health and chemicals in the home as well as how to boost their health naturally through nutrition. We show people how to eliminate those toxins and share the message with others.
We also work with and mentor people who want to build their own business, share the message and create a leveraged income.
Our business name is: Brivora
The tag line we have is: Simple Changes ยท Healthy Living
Output for the project is:
Logo and business card design (2 people on the card).
Our perspective is for a modern, natural, simple, clean design (web 2.0 feel) that will appeal to a broad age range and audience. It should feel professional but not formal. It should not seem medical.
The logo should not be a gradient nor overly complex. Colouring should only be one or two colours at most. They can be bright, we are tending to lean towards green for obvious reasons but open to your thoughts.
Simplicity is the key.
The business card needs to be two sided. We like having the logo and card details on the front and then reversed out on the back with the logo and name in white on the colour block.
Please see the attached card brief document about the card content.

```html
<!DOCTYPE html>
<html lang="en">
<head>
<meta charset="utf-8">
<title>Brivora – Business Card</title>
<link href="https://fonts.googleapis.com/css2?family=Noto+Serif:wght@400&display=swap" rel="stylesheet">
<style>
  :root {
    --green: #2c9a0c;
    --green-light: #74c553;
    --green-text: #3a9a1e;
    --band: #d9eed3;
    --ink: #111111;
    --white: #ffffff;
    --border: #9a9a9a;
  }
  * { box-sizing: border-box; margin: 0; padding: 0; }
  html, body {
    width: 1200px; height: 900px; overflow: hidden;
    background: var(--white);
    font-family: "Noto Serif", Georgia, serif;
  }
  .canvas { position: relative; width: 1200px; height: 900px; }

  /* Front side */
  .card-front {
    position: absolute; left: 42px; top: 24px; width: 720px; height: 416px;
  }
  .card-front__hero {
    position: absolute; left: 0; top: 0; width: 100%; height: 308px;
    background: radial-gradient(ellipse 60% 80% at 40% 40%, var(--green-light) 0%, var(--green) 75%);
  }
  .brand--front {
    position: absolute; left: 134px; top: 118px;
    font-size: 100px; line-height: 1; color: var(--white); letter-spacing: -1px;
  }
  .tagline--front {
    position: absolute; left: 150px; top: 222px;
    font-size: 26px; color: var(--ink);
  }
  .card-front__benefits {
    position: absolute; left: 0; top: 312px; width: 100%; height: 104px;
    background: var(--band);
  }
  .benefit-list {
    position: absolute; list-style: none;
    font-size: 13px; color: var(--green-text);
  }
  .benefit-list li { position: relative; padding-left: 12px; height: 21px; line-height: 21px; }
  .benefit-list li::before {
    content: ""; position: absolute; left: 0; top: 8px;
    width: 6px; height: 6px; border-radius: 50%; background: var(--ink);
  }
  .benefit-list--one { left: 10px; top: 22px; }
  .benefit-list--two { left: 290px; top: 22px; }
  .benefit-list--three { left: 578px; top: 16px; }
  .benefit-list--three li { height: 17px; line-height: 17px; }
  .benefit-list--three li::before { top: 6px; }

  /* Back side */
  .card-back {
    position: absolute; left: 450px; top: 460px; width: 710px; height: 420px;
    border: 1px solid var(--border); background: var(--white);
  }
  .card-back__logo {
    position: absolute; left: 0; top: 42px; width: 100%; text-align: center;
  }
  .brand--back { font-size: 44px; line-height: 1; color: var(--green); }
  .tagline--back { font-size: 12px; color: var(--ink); margin-top: 2px; }
  .person { position: absolute; top: 142px; }
  .person--one { left: 46px; }
  .person--two { left: 502px; }
  .person__name { font-size: 28px; color: var(--ink); line-height: 1.2; }
  .person__mobile { font-size: 13px; color: var(--ink); }
  .label { color: var(--green-text); }
  .contact {
    position: absolute; left: 180px; top: 270px; width: 330px;
    font-size: 14px; color: var(--ink);
  }
  .contact__address { display: flex; gap: 6px; }
  .contact__line { margin-top: 10px; text-align: center; padding-right: 50px; }
  .card-back__footer {
    position: absolute; left: 0; bottom: 0; width: 100%; height: 26px;
    background: var(--green); color: var(--white);
    font-size: 14px; line-height: 26px; text-align: center;
  }
</style>
</head>
<body>
<main class="canvas">

  <section class="card-front" aria-label="Card front">
    <div class="card-front__hero">
      <div class="brand brand--front">Brivora</div>
      <div class="tagline tagline--front">Small Steps · Natural Wellness</div>
    </div>
    <div class="card-front__benefits">
      <ul class="benefit-list benefit-list--one">
        <li>Multiple Streams of Income</li>
        <li>Financial Freedom</li>
        <li>Own my Own Business</li>
      </ul>
      <ul class="benefit-list benefit-list--two">
        <li>More Time</li>
        <li>Personal Development</li>
        <li>Health and Vitality</li>
      </ul>
      <ul class="benefit-list benefit-list--three">
        <li>Help Others</li>
        <li>Meet New People</li>
        <li>Retirement Plan</li>
        <li>Leave a Legacy</li>
      </ul>
    </div>
  </section>

  <section class="card-back" aria-label="Card back">
    <div class="card-back__logo">
      <div class="brand brand--back">Brivora</div>
      <div class="tagline tagline--back">Small Steps · Natural Wellness</div>
    </div>

    <div class="person person--one">
      <div class="person__name">Name1</div>
      <div class="person__mobile"><span class="label">Mobile:</span>0000000000</div>
    </div>
    <div class="person person--two">
      <div class="person__name">Name2</div>
      <div class="person__mobile"><span class="label">Mobile:</span>0000000000</div>
    </div>

    <div class="contact">
      <div class="contact__address">
        <span class="label">Address:</span>
        <span>xxxxxxxxxxxxxxxxxxxxxx<br>xxxxxxxxxxxxxxxxxxxxxxxx</span>
      </div>
      <div class="contact__line"><span class="label">Phone:</span>000 000 000</div>
      <div class="contact__line"><span class="label">Email:</span>xxxxxxxx</div>
    </div>

    <div class="card-back__footer">www.livebrivora.com</div>
  </section>

</main>
</body>
</html>
```